Need App for Impact Related Events

My app is to help with internal events. When you enter the prompted event code the next screen shows you everyone currently at the event. It will give you the ability to Start a conversation with someone you met at that event, or signal it is your turn to send a message. The next screen is a message thread with that person. I am looking for a design that incorporates the colors and ‘feel good’ emotion of our logo. I have pieced together a pretty good interpretation of what I’m looking for in the attached mockup by slicing and dicing designs. I also attached our logo mascot.Screens (see attached mockups)

Note 1: I do not like the picture on the screen used in screen one because it makes it seem like a dating app. I attached an alternative photo that can be used or present different ideas.

Note 2: On the login/signup screen (screen 2) I need an additional first and last name for login, you can try to fit this on one login screen or present a two step signup screen where that is presented in the second screen.

READ MOCKUP GUIDELINES UNDER Must Haves

Target Market(s)

People attending internal social impact events

Industry/Entity Type

Charity

Font styles to use
Sans Serif

Colors
86cfc6

Requirements
Must have
• Follow the screen mockups attached to project
• PLEASE READ
• I have provided a relatively close design of what I’m looking for in the mockups. Some screens need to be followed more closely to my design mockup than other. I have listed a guide below how how closely you should follow my mockup design exactly. Overall I would like to see some ideas of incorporating a few accent colors so it doesn’t appear SO Blue. I also attached some app inspiration designs I found from around the web
• Screen Mockup Guideline Follow %
• Screen 1: 65% - mostly on target, would like to see ways to make it not SO Blue and possibly creative places to add some explainer text describing the app
• Screen 2: 50% - general design idea is here, but more open
• Screen 3: 35% - a lot more room for design influence
• Screen 4: 70% - mostly on target, a little room for design influence/color scheme ideas
• Screen 5-6: 25% - a lot of room for design change/ideas/influence
• Screen 7-8: 80% - already very close to what I need, maybe open to slight sizing and color scheme ideas
• Screen 9: 15% - the most open for influence, only the general functionality of the screen is communicated here
Nice to have
• Please Read Mockup Guideline above. In large part I am looking for something to use some nice accent colors so it is not overwhelmingly blue and bring the whole design into a seamless style.
Should not have

```html
<!DOCTYPE html>
<html lang="en">
<head>
<meta charset="utf-8">
<title>Hivewell – Welcome and Event Code Screens</title>
<link href="https://fonts.googleapis.com/css2?family=Josefin+Sans:wght@300;400;600;700&family=Lato:wght@400&display=swap" rel="stylesheet">
<style>
  :root {
    --page: #ffffff;
    --ink: #1c1c1c;
    --muted: #7b7f86;
    --placeholder: #c3c8cf;
    --rule: #d9dde2;
    --mint: #52ffe6;
    --sky: #85b8fb;
    --link: #46aef2;
    --btn-start: #a3a6fb;
    --btn-end: #12e6f0;
    --mist: #f5f9fd;
    --glow: rgba(70, 225, 240, 0.22);
    --photo-a: #c9d3da;
    --photo-b: #e8eef1;
    --photo-c: #b58e78;
  }
  * { box-sizing: border-box; margin: 0; padding: 0; }
  html, body { width: 1200px; height: 768px; overflow: hidden; background: var(--page); }
  body { position: relative; font-family: "Josefin Sans", sans-serif; color: var(--ink); }

  .screen {
    position: absolute;
    width: 300px; height: 534px;
    background: var(--page);
    overflow: hidden;
    box-shadow: 0 12px 40px var(--glow), 0 0 24px var(--glow);
  }
  .screen--welcome { left: 284px; top: 62px; }
  .screen--code { left: 610px; top: 198px; }

  .status-bar {
    position: absolute; left: 0; top: 0; width: 100%; height: 20px;
    font-family: "Lato", sans-serif; font-size: 9px; color: var(--ink);
    z-index: 5;
  }
  .status-bar__signal { position: absolute; left: 6px; top: 4px; }
  .status-bar__time { position: absolute; left: 0; right: 0; top: 5px; text-align: center; }
  .status-bar__battery { position: absolute; right: 6px; top: 4px; display: flex; align-items: center; gap: 3px; }

  .hero-photo {
    position: absolute; left: 0; top: 0; width: 300px; height: 222px;
    background: linear-gradient(120deg, var(--photo-b) 0%, var(--photo-a) 40%, var(--photo-c) 60%, var(--photo-b) 100%);
  }
  .hero-cloud { position: absolute; left: 0; top: 140px; width: 300px; height: 100px; }

  .brand-badge {
    position: absolute; left: 116px; top: 156px; width: 68px; height: 68px;
    border-radius: 50%; background: var(--page);
    box-shadow: 0 2px 10px rgba(0,0,0,0.08);
    display: flex; align-items: center; justify-content: center;
  }
  .brand-name { font-family: "Josefin Sans", sans-serif; font-weight: 700; font-size: 13px; color: #1a9fb0; }
  .brand-name--large { font-size: 20px; }

  .tagline {
    position: absolute; left: 0; right: 0; top: 250px;
    text-align: center; font-size: 19px; font-weight: 400; letter-spacing: 0.5px;
  }

  .pill-button {
    position: absolute; left: 100px; width: 100px; height: 37px;
    border-radius: 19px;
    background: linear-gradient(90deg, var(--btn-start), var(--btn-end));
    box-shadow: 0 6px 14px rgba(60, 200, 240, 0.3);
    color: #fff; font-weight: 700; font-size: 12px;
    display: flex; align-items: center; justify-content: center; padding-top: 2px;
  }
  .text-link {
    position: absolute; left: 0; right: 0; text-align: center;
    font-weight: 700; font-size: 12px; color: var(--link); text-decoration: underline;
  }

  .waves { position: absolute; left: 0; bottom: 0; width: 300px; height: 170px; }

  .mist { position: absolute; left: 0; top: 140px; width: 300px; height: 394px; }

  .settings-icon { position: absolute; left: 261px; top: 44px; }
  .code-brand { position: absolute; left: 0; right: 0; top: 88px; text-align: center; }

  .code-title {
    position: absolute; left: 0; right: 0; top: 165px; text-align: center;
    font-weight: 300; font-size: 18px; color: var(--muted); letter-spacing: 0.5px;
  }
  .code-input {
    position: absolute; left: 77px; top: 216px; width: 146px; height: 22px;
    border-bottom: 1px solid var(--rule);
    font-family: "Lato", sans-serif; font-size: 10px; color: var(--placeholder);
    text-align: center;
  }
</style>
</head>
<body>

<section class="screen screen--welcome">
  <div class="status-bar" style="color:#222">
    <svg class="status-bar__signal" width="30" height="9" viewBox="0 0 30 9">
      <rect x="0" y="6" width="2" height="3" fill="#222"/><rect x="3" y="4" width="2" height="5" fill="#222"/>
      <rect x="6" y="2" width="2" height="7" fill="#222"/><rect x="9" y="0" width="2" height="9" fill="#222"/>
      <path d="M15 3.5a7 7 0 0 1 10 0M17 5.5a4 4 0 0 1 6 0" stroke="#222" stroke-width="1.3" fill="none"/>
      <circle cx="20" cy="7.5" r="1" fill="#222"/>
    </svg>
    <span class="status-bar__time">9:41 AM</span>
    <span class="status-bar__battery">✱ 100%
      <svg width="20" height="8" viewBox="0 0 20 8"><rect x="0.5" y="0.5" width="17" height="7" rx="1" fill="none" stroke="#222"/><rect x="2" y="2" width="14" height="4" fill="#222"/><rect x="18" y="2.5" width="1.5" height="3" fill="#222"/></svg>
    </span>
  </div>

  <div class="hero-photo" role="img" aria-label="Photo of event attendees smiling together in a bright café"></div>
  <svg class="hero-cloud" viewBox="0 0 300 100" preserveAspectRatio="none">
    <path d="M0 20 C 30 0, 110 0, 150 30 C 180 10, 220 20, 240 40 C 260 28, 275 45, 300 80 L300 100 L0 100 Z" fill="#fff"/>
  </svg>

  <div class="brand-badge"><span class="brand-name">Hivewell</span></div>

  <h1 class="tagline">Be nice. Be Kind</h1>
  <div class="pill-button" style="top:306px">Sign In</div>
  <div class="text-link" style="top:366px">Sign Up</div>

  <svg class="waves" viewBox="0 0 300 170">
    <path d="M0 45 L10 50 L0 62 Z" fill="var(--sky)"/>
    <path d="M120 70 C 160 52, 190 22, 225 22 C 255 22, 270 56, 300 70 L300 140 L120 140 Z" fill="var(--sky)"/>
    <path d="M0 58 C 20 36, 38 7, 56 7 C 80 7, 110 46, 132 60 C 150 72, 150 76, 160 88 C 180 121, 200 136, 232 131 C 260 126, 285 111, 300 94 L300 170 L0 170 Z" fill="var(--mint)"/>
  </svg>
</section>

<section class="screen screen--code">
  <svg class="mist" viewBox="0 0 300 394" preserveAspectRatio="none">
    <path d="M0 26 C 30 8, 70 0, 100 6 C 160 18, 240 14, 270 40 C 285 55, 290 70, 300 78 L300 394 L0 394 Z" fill="var(--mist)"/>
  </svg>

  <div class="status-bar">
    <svg class="status-bar__signal" width="30" height="9" viewBox="0 0 30 9">
      <rect x="0" y="6" width="2" height="3" fill="#222"/><rect x="3" y="4" width="2" height="5" fill="#222"/>
      <rect x="6" y="2" width="2" height="7" fill="#222"/><rect x="9" y="0" width="2" height="9" fill="#222"/>
      <path d="M15 3.5a7 7 0 0 1 10 0M17 5.5a4 4 0 0 1 6 0" stroke="#222" stroke-width="1.3" fill="none"/>
      <circle cx="20" cy="7.5" r="1" fill="#222"/>
    </svg>
    <span class="status-bar__time">9:41 AM</span>
    <span class="status-bar__battery">✱ 100%
      <svg width="20" height="8" viewBox="0 0 20 8"><rect x="0.5" y="0.5" width="17" height="7" rx="1" fill="none" stroke="#222"/><rect x="2" y="2" width="14" height="4" fill="#222"/><rect x="18" y="2.5" width="1.5" height="3" fill="#222"/></svg>
    </span>
  </div>

  <svg class="settings-icon" width="18" height="18" viewBox="0 0 24 24" aria-label="Settings">
    <path fill="#111" d="M19.4 13a7.5 7.5 0 0 0 0-2l2.1-1.6-2-3.5-2.5 1a7.6 7.6 0 0 0-1.7-1L15 3h-4l-.4 2.9a7.6 7.6 0 0 0-1.7 1l-2.5-1-2 3.5L6.6 11a7.5 7.5 0 0 0 0 2l-2.1 1.6 2 3.5 2.5-1a7.6 7.6 0 0 0 1.7 1L11 21h4l.4-2.9a7.6 7.6 0 0 0 1.7-1l2.5 1 2-3.5ZM13 15.5A3.5 3.5 0 1 1 13 8.5a3.5 3.5 0 0 1 0 7Z" transform="translate(-1 0)"/>
  </svg>

  <div class="code-brand"><span class="brand-name brand-name--large">Hivewell</span></div>

  <h2 class="code-title">location kind code</h2>
  <div class="code-input">Type Here</div>
  <div class="pill-button" style="top:269px">Enter Code</div>
  <div class="text-link" style="top:332px">Create own code</div>

  <svg class="waves" viewBox="0 0 300 170">
    <path d="M0 45 L10 50 L0 62 Z" fill="var(--sky)"/>
    <path d="M120 70 C 160 52, 190 22, 225 22 C 255 22, 270 56, 300 70 L300 140 L120 140 Z" fill="var(--sky)"/>
    <path d="M0 58 C 20 36, 38 7, 56 7 C 80 7, 110 46, 132 60 C 150 72, 150 76, 160 88 C 180 121, 200 136, 232 131 C 260 126, 285 111, 300 94 L300 170 L0 170 Z" fill="var(--mint)"/>
  </svg>
</section>

</body>
</html>
```